NEW Modern Sleek Business Card for VR Language Startup

Our startup is using VR to lead the next wave of world language education. We need a two-sided business card that introduces the larger organization (Quorvel Language Inc) and our contact info on one side and shows the product, Lumidrasca, on the other side.

Side 1 (contact info)= Quorvel Logo and Contact info (name, title, phone, email)

Side 2 (product)= Lumidrasc logo, text, and website
Text= Culturally Immersive Language Learning Games
Website= www.lumidrasc.example

Target Market(s)

Education, Technology

Contact Information for Business Card

Contact info will be updated upon approval of the design. For now, put this as a placeholder.

Perry Hollins
Founder & CEO
phollins@mailtrove.example
(555)-014-2736

Font styles to use
Other font styles liked:
• Gibson and Century Gothic are the brand fonts

Requirements
Nice to have
• I would love to see cohesion between the design and colors of the two logos. I have attached a few business card designs that I like, so you can get a feel for my preferred style.

```html
<!DOCTYPE html>
<html lang="en">
<head>
<meta charset="utf-8">
<title>Quorvel Language – Business Cards</title>
<link href="https://fonts.googleapis.com/css2?family=Lato:wght@400;700&display=swap" rel="stylesheet">
<style>
  :root {
    --page-bg: #eeeae8;
    --card-white: #ffffff;
    --orange: #f7a234;
    --coral: #f6733a;
    --violet: #7d5ce6;
    --indigo: #6a5cf0;
    --sky: #3fa6ec;
    --cyan: #22d8ea;
    --ink: #1c1c1c;
    --ink-soft: #3c3c3c;
    --divider-dark: #111111;
    --divider-grey: #555a66;
    --on-gradient: #ffffff;
  }
  * { box-sizing: border-box; margin: 0; padding: 0; }
  html, body { width: 1200px; height: 953px; overflow: hidden; }
  body {
    background: var(--page-bg);
    font-family: "Lato", sans-serif;
    position: relative;
  }
  .card {
    position: absolute;
    width: 462px;
    height: 286px;
    display: flex;
    background: var(--card-white);
    box-shadow: 0 6px 18px rgba(0,0,0,0.12);
  }
  .card--contact { left: 288px; top: 175px; }
  .card--product { left: 481px; top: 483px; }

  .card__panel {
    width: 228px;
    height: 100%;
    color: var(--on-gradient);
    position: relative;
  }
  .card--contact .card__panel {
    background: linear-gradient(180deg, var(--orange) 0%, var(--coral) 28%, var(--violet) 55%, var(--indigo) 70%, var(--sky) 85%, var(--cyan) 100%);
  }
  .card--product .card__panel {
    background: linear-gradient(180deg, var(--cyan) 0%, var(--sky) 45%, var(--indigo) 100%);
  }
  .card__divider { width: 3px; height: 100%; }
  .card--contact .card__divider { background: var(--divider-dark); }
  .card--product .card__divider { background: var(--divider-grey); }

  .card__brand {
    flex: 1;
    display: flex;
    flex-direction: column;
    align-items: center;
    justify-content: center;
    gap: 14px;
  }
  .brand-dot {
    width: 56px; height: 56px;
    border-radius: 50%;
    background: var(--violet);
  }
  .card--product .brand-dot { width: 96px; height: 96px; background: var(--sky); }
  .brand-name {
    font-family: "Lato", sans-serif;
    font-weight: 700;
    color: var(--ink);
    letter-spacing: 0.14em;
    font-size: 30px;
    text-transform: uppercase;
  }
  .card--product .brand-name {
    letter-spacing: 0;
    text-transform: none;
    font-weight: 400;
    color: var(--ink-soft);
    font-size: 34px;
  }

  .contact__name {
    position: absolute; left: 27px; top: 106px;
    font-weight: 700; font-size: 18px; text-transform: uppercase; letter-spacing: -0.01em;
  }
  .contact__title {
    position: absolute; left: 27px; top: 127px;
    font-size: 13px;
  }
  .contact__list {
    position: absolute; left: 27px; top: 182px;
    list-style: none; font-size: 13px; line-height: 18px;
  }
  .contact__list li { display: flex; align-items: center; gap: 4px; }
  .contact__list svg { width: 11px; height: 11px; fill: var(--on-gradient); }

  .product__tagline {
    position: absolute; left: 28px; top: 110px;
    font-size: 13.5px; line-height: 21px; text-transform: uppercase;
  }
  .product__url {
    position: absolute; left: 28px; top: 197px;
    font-size: 14px;
  }
</style>
</head>
<body>
  <section class="card card--contact" aria-label="Contact side">
    <div class="card__panel">
      <p class="contact__name">Perry Hollins</p>
      <p class="contact__title">Founder &amp; CEO</p>
      <ul class="contact__list">
        <li><svg viewBox="0 0 12 12" aria-hidden="true"><path d="M1 4c0-2 2-3 5-3s5 1 5 3l-2 1-1-1.5H4L3 5zM3 6h6l1.5 4.5h-9z"/></svg>(555)-014-2736</li>
        <li><svg viewBox="0 0 12 12" aria-hidden="true"><path d="M1 2.5h10v7H1zM1.8 3.2 6 6.6l4.2-3.4v-.2H1.8z" fill-rule="evenodd"/></svg>phollins@mailtrove.example</li>
      </ul>
    </div>
    <div class="card__divider"></div>
    <div class="card__brand">
      <span class="brand-dot"></span>
      <span class="brand-name">Quorvel</span>
    </div>
  </section>

  <section class="card card--product" aria-label="Product side">
    <div class="card__panel">
      <p class="product__tagline">Culturally immersive<br>language<br>learning games</p>
      <p class="product__url">www.lumidrasc.example</p>
    </div>
    <div class="card__divider"></div>
    <div class="card__brand">
      <span class="brand-dot"></span>
      <span class="brand-name">Lumidrasc</span>
    </div>
  </section>
</body>
</html>
```